DL Flyer for conservation/restoration business

I am an objects conservator and run a business called RelicCare Studio. I specialise in conserving and restoring 3 dimensional artworks and artefacts in Perth, Western Australia. I dont work on paintings, paper or textiles but pretty much everything else such as sculptures, metal, wood, ceramics etc. So far I have been reasonably successful in marketing to small museums and councils. However, I would like to pick up some more work from private individuals living in the more affluent areas of Perth.

I would like to have a DL flyer designed to do a letterbox drop in my target areas. I would like something professional and eyecatching that wont get thrown away. Also it will make the business look trustworthy.

I would like to have something that will go with my existing logo if possible.

Target Market(s)

wealthy individuals over 50 who enjoy collecting art / antiques

Industry/Entity Type

Marketing

Requirements
Must have
• I would like a good background image or images of suitable artworks/ artefacts/ conservator at work (hands only). Also include my logo as the business name.

I am happy to take advice on advertising, but my preference is for the text in the attached word file (order can be rearranged):

I would like to be able to edit the flyer if necessary at a later date, and would like it to be compatible with MS Publisher.
Should not have
• Do not include any images of paintings, textiles, paper or books.

```html
<!DOCTYPE html>
<html lang="en">
<head>
<meta charset="utf-8">
<title>RelicCare Studio – DL Flyer</title>
<link rel="stylesheet" href="https://fonts.googleapis.com/css2?family=Crimson+Text:ital,wght@0,400;1,400&family=Open+Sans:wght@400;600;700&display=swap">
<style>
  :root {
    --navy: #1f2f4d;
    --ink: #14223a;
    --red: #a3262b;
    --panel: #050505;
    --white: #ffffff;
    --bg-top: #ffffff;
    --bg-mid: #e3ebf2;
    --bg-low: #b9cad9;
  }
  html, body {
    margin: 0;
    padding: 0;
    width: 1200px;
    height: 2400px;
    overflow: hidden;
    background: #ffffff;
  }
  .flyer {
    position: relative;
    width: 1200px;
    height: 2400px;
    overflow: hidden;
    background:
      radial-gradient(ellipse at 85% 35%, rgba(160,185,210,0.55), transparent 55%),
      radial-gradient(ellipse at 10% 90%, rgba(150,175,200,0.6), transparent 50%),
      linear-gradient(180deg, var(--bg-top) 0%, var(--bg-top) 12%, var(--bg-mid) 35%, #d2dfea 70%, var(--bg-low) 100%);
    font-family: "Open Sans", Arial, sans-serif;
    color: var(--ink);
  }
  .brand {
    position: absolute;
    top: 110px;
    left: 150px;
    display: flex;
    align-items: center;
    gap: 34px;
  }
  .brand-mark {
    width: 150px;
    height: 150px;
  }
  .brand-name {
    font-weight: 700;
    font-size: 88px;
    color: var(--navy);
    letter-spacing: 1px;
    line-height: 1;
  }
  .tagline {
    position: absolute;
    top: 420px;
    left: 70px;
    right: 70px;
    margin: 0;
    text-align: center;
    font-family: "Crimson Text", Georgia, serif;
    font-style: italic;
    font-size: 54px;
    line-height: 1.2;
    color: var(--red);
  }
  .services {
    position: absolute;
    top: 635px;
    left: 58px;
    right: 60px;
    font-size: 46px;
    line-height: 1.32;
    color: var(--ink);
  }
  .services p { margin: 0; }
  .services ul {
    margin: 0;
    padding-left: 50px;
  }
  .services li { margin: 0; }
  .portfolio {
    position: absolute;
    top: 1088px;
    left: 54px;
    width: 1092px;
    height: 1020px;
    background: var(--panel);
    border-radius: 0 0 34px 34px;
    box-sizing: border-box;
    padding: 0 4px;
  }
  .portfolio-title {
    margin: 0;
    height: 85px;
    line-height: 85px;
    text-align: center;
    font-family: "Crimson Text", Georgia, serif;
    font-style: italic;
    font-weight: 400;
    font-size: 56px;
    color: var(--white);
  }
  .work-grid {
    display: grid;
    grid-template-columns: repeat(3, 1fr);
    column-gap: 30px;
    row-gap: 28px;
  }
  .work { margin: 0; }
  .work-photo {
    display: block;
    width: 100%;
    height: 300px;
  }
  .work figcaption {
    background: var(--white);
    color: var(--red);
    font-size: 21px;
    text-align: center;
    line-height: 32px;
    height: 32px;
  }
  .photo-sculpture { background: linear-gradient(160deg, #8fa9c4 0%, #5d6a73 55%, #3e4a3c 100%); }
  .photo-crest { background: linear-gradient(180deg, #7a2626 0%, #4f6e58 45%, #8a3a2c 100%); }
  .photo-statue { background: linear-gradient(170deg, #cfd9e0 0%, #7c7c70 50%, #4d5a3e 100%); }
  .photo-plaza { background: linear-gradient(180deg, #6d7a86 0%, #a9a8a2 50%, #8d8b84 100%); }
  .photo-figure { background: linear-gradient(180deg, #7fa4c8 0%, #6f8d5a 55%, #5d7d48 100%); }
  .photo-bronze { background: linear-gradient(170deg, #9aa6ae 0%, #5c5651 55%, #7d8470 100%); }
  .quote-line {
    margin: 0;
    padding-top: 125px;
    text-align: center;
    font-family: "Crimson Text", Georgia, serif;
    font-style: italic;
    font-size: 56px;
    line-height: 1.2;
    color: var(--white);
  }
  .contact {
    position: absolute;
    top: 2128px;
    left: 0;
    right: 0;
    text-align: center;
    font-size: 42px;
    line-height: 1.36;
    color: var(--ink);
  }
  .contact-heading { font-weight: 700; }
  .contact p { margin: 0; }
</style>
</head>
<body>
  <main class="flyer">
    <header class="brand">
      <svg class="brand-mark" viewBox="0 0 100 100" aria-hidden="true">
        <circle cx="50" cy="50" r="46" fill="#1f2f4d"/>
      </svg>
      <span class="brand-name">RelicCare Studio</span>
    </header>

    <p class="tagline">University trained conservator with over 20 years’ experience in major galleries and museums.</p>

    <section class="services">
      <p>Conservation and restoration of objects including:</p>
      <ul>
        <li>Historical items, antiques, ceramics and sculpture</li>
        <li>Custom made display fittings and supports.</li>
        <li>Free advice on storage and display techniques to help preserve your treasured items.</li>
      </ul>
    </section>

    <section class="portfolio">
      <h2 class="portfolio-title">Some of Our Work</h2>
      <div class="work-grid">
        <figure class="work">
          <div class="work-photo photo-sculpture" role="img" aria-label="Photo of an angular dark metal outdoor sculpture under blue sky"></div>
          <figcaption>Dark Monolith</figcaption>
        </figure>
        <figure class="work">
          <div class="work-photo photo-crest" role="img" aria-label="Photo of a restored green and gold crest on a red wall"></div>
          <figcaption>Civic Crest</figcaption>
        </figure>
        <figure class="work">
          <div class="work-photo photo-statue" role="img" aria-label="Photo of a bronze standing statue on a stone plinth"></div>
          <figcaption>Founder's Statue</figcaption>
        </figure>
        <figure class="work">
          <div class="work-photo photo-plaza" role="img" aria-label="Photo of white block sculptures in a building forecourt"></div>
          <figcaption>Convergence</figcaption>
        </figure>
        <figure class="work">
          <div class="work-photo photo-figure" role="img" aria-label="Photo of a bronze seated figure with a dog on a lawn"></div>
          <figcaption>Northern Passage</figcaption>
        </figure>
        <figure class="work">
          <div class="work-photo photo-bronze" role="img" aria-label="Photo of a bronze sculpture of a mother and child"></div>
          <figcaption>Mother and Child</figcaption>
        </figure>
      </div>
      <p class="quote-line">Offering free quotes in your area on:</p>
    </section>

    <footer class="contact">
      <p class="contact-heading">Contact:</p>
      <p>Helena Marsh | 9555 0142 / 0400 555 318</p>
      <p>studio@reliccarestudio.com</p>
      <p>www.reliccarestudio.com</p>
    </footer>
  </main>
</body>
</html>
```